Healthcare technology company website - Tralom

Create wireframe design for Tralom, an Australian based medical technology company developing a robotic ultrasound system.

Current site tralom.com
https://www.plandeck.example/proto/k7pLwQ2zR9dXmB4nC8vT5E/Tralom-Website?node-id=2210-3381&t=aBcDeFgHiJkLmNoP-1.
https://www.plandeck.example/proto/k7pLwQ2zR9dXmB4nC8vT5E/Tralom-Website?page-id=2207%3A518&node-id=2233-4410&viewport=-33%2C513%2C0.15&t=QrStUvWxYzAbCdEf-1&scaling=min-zoom&content-scaling=fixed&starting-point-node-id=2233%3A4410
The attached mp4 to be the hero view. Open to designer who can improve it. Attached figma

Industry/Entity Type

tech healthcare

Number of Pages Required

4 page

Requirements
Must have
• Hero view with mp4 attached. Hardware interaction model similar to https://www.quorvin.example/au/sonebuds-4/ div class="section section-redesigned no-pad-bottom will-change"

```html
<!DOCTYPE html>
<html lang="en">
<head>
<meta charset="utf-8">
<title>Tralom — Vascular Imaging, Reimagined</title>
<link href="https://fonts.googleapis.com/css2?family=Plus+Jakarta+Sans:wght@300;400;500;600;700&display=swap" rel="stylesheet">
<style>
:root{
  --ink:#161616;
  --ink-soft:#4a4a4a;
  --dark:#262626;
  --white:#ffffff;
  --card:#ffffff;
  --card-soft:#f6fafc;
  --icon-bg:#c9dfeb;
  --line:#bdbdbd;
  --purple:#7b4fe0;
  --pink:#c74fb6;
  --blue-glow:#d6ecf8;
  --pink-glow:#fbe1de;
}
*{box-sizing:border-box;margin:0;padding:0}
html,body{width:1200px;height:2769px;overflow:hidden;background:var(--white)}
body{font-family:"Plus Jakarta Sans",sans-serif;color:var(--ink)}
.page{position:relative;width:1200px;height:2769px;overflow:hidden}
.abs{position:absolute}
.btn-dark{position:absolute;display:flex;align-items:center;justify-content:center;background:var(--dark);color:var(--white);font-size:12px;font-weight:600;border-radius:20px}
.btn-outline{position:absolute;display:flex;align-items:center;justify-content:center;border:1.3px solid var(--ink);color:var(--ink);font-size:12px;font-weight:600;border-radius:20px;background:var(--white)}
.btn-outline-light{position:absolute;display:flex;align-items:center;justify-content:center;border:1.3px solid var(--white);color:var(--white);font-size:12px;font-weight:600;border-radius:20px}

/* hero */
.hero-glow{position:absolute;left:0;top:0;width:1200px;height:560px;
  background:
   radial-gradient(circle at 330px 240px,var(--blue-glow) 0,rgba(214,236,248,.6) 150px,rgba(255,255,255,0) 300px),
   radial-gradient(circle at 880px 240px,var(--pink-glow) 0,rgba(251,225,222,.6) 150px,rgba(255,255,255,0) 300px),
   radial-gradient(circle at 600px 420px,rgba(214,236,248,.7) 0,rgba(255,255,255,0) 180px);}
.nav-logo{left:173px;top:20px;font-size:30px;font-weight:300;letter-spacing:1px;line-height:30px}
.nav-links{left:509px;top:28px;display:flex;gap:20px;font-size:12px;font-weight:500}
.nav-cta{left:922px;top:18px;width:105px;height:34px;border:1.3px solid var(--ink);border-radius:20px;display:flex;align-items:center;justify-content:center;font-size:12px;font-weight:600}
.hero-mark{left:0;width:1200px;top:150px;text-align:center;font-size:150px;font-weight:300;line-height:140px;letter-spacing:6px}
.hero-title{left:0;width:1200px;top:306px;text-align:center;font-size:43px;font-weight:700;
  background:linear-gradient(90deg,var(--purple),var(--pink));-webkit-background-clip:text;background-clip:text;color:transparent}
.hero-sub{left:0;width:1200px;top:361px;text-align:center;font-size:12px;font-weight:600;line-height:18px}

.partners{left:173px;top:461px;width:854px;height:110px;background:var(--dark);border-radius:55px;display:flex;align-items:center;justify-content:space-around;padding:0 20px;color:var(--white);font-size:12px;font-weight:600;letter-spacing:.4px}

/* about */
.about-photo{left:173px;top:664px;width:366px;height:307px;border-radius:20px;background:radial-gradient(ellipse at 40% 40%,#f2a7a0 0,#de4b45 45%,#a8231f 100%)}
.about-title{left:577px;top:676px;width:450px;font-size:28px;font-weight:600;line-height:32px}
.body-text{font-size:11.5px;line-height:17.5px;color:var(--ink-soft);font-weight:400}
.about-text{left:577px;top:747px;width:452px}

.section-title{left:0;width:1200px;text-align:center;font-size:26px;font-weight:600}

/* solutions */
.solution{position:absolute;top:1107px;width:268px;height:231px;background:var(--card);border-radius:16px;box-shadow:0 2px 14px rgba(0,0,0,.06);text-align:center}
.solution .icon{position:absolute;left:103px;top:22px;width:62px;height:62px;border-radius:50%;background:var(--icon-bg);display:flex;align-items:center;justify-content:center}
.solution h3{position:absolute;top:100px;width:100%;font-size:16px;font-weight:500}
.solution p{position:absolute;top:128px;left:24px;right:24px;font-size:12px;line-height:17.5px;color:var(--ink-soft)}
.solution .btn-outline{left:85px;top:178px;width:97px;height:32px}
.burst{position:absolute;border-radius:50%;background:radial-gradient(circle,rgba(190,220,238,.55) 0,rgba(214,236,248,.25) 50%,rgba(255,255,255,0) 70%)}

/* products */
.product{position:absolute;top:1475px;width:414px;height:217px;background:var(--dark);border-radius:30px;color:var(--white)}
.product .art{position:absolute;left:16px;top:24px;width:175px;height:170px;border-radius:50%}
.product h3{position:absolute;left:209px;top:18px;font-size:19px;font-weight:600}
.product p{position:absolute;left:209px;top:46px;width:190px;font-size:11.5px;line-height:17.5px;color:#eaeaea}
.product .btn-outline-light{left:209px;top:163px;width:93px;height:32px}

/* vision */
.vision{left:173px;top:1787px;width:854px;height:314px;background:var(--card-soft);border-radius:20px;box-shadow:0 2px 14px rgba(0,0,0,.04)}
.vision-art{left:47px;top:30px;width:258px;height:253px;border-radius:50%;background:radial-gradient(circle at 45% 40%,#8e90ef 0,#4c4fd6 55%,#2a2c9a 100%)}
.vision-title{left:353px;top:40px;font-size:28px;font-weight:700}
.vision-text{left:353px;top:82px;width:440px}

/* contact */
.contact-title{left:173px;top:2184px;font-size:27px;font-weight:600}
.label{position:absolute;left:174px;font-size:11px;font-weight:500;letter-spacing:.3px}
.field{position:absolute;left:174px;width:391px;height:36px;border:1px solid var(--line);border-radius:4px;font-size:10px;color:#8a8a8a;display:flex;align-items:center;padding-left:12px}
.phone-code{position:absolute;left:0;top:0;width:70px;height:34px;background:#f1f1f1;border-right:1px solid var(--line);display:flex;align-items:center;justify-content:center;gap:4px;font-size:10px}
.flag{width:13px;height:9px;background:linear-gradient(#f29a3a 0 33%,#fff 33% 66%,#2f9a48 66%)}
.check{left:174px;top:2438px;display:flex;align-items:center;gap:8px;font-size:12.5px;color:#7a7a7a}
.check span{width:14px;height:14px;border:1px solid #999;border-radius:2px;display:inline-block}
.photo{position:absolute;border-radius:10px}

/* footer */
.footer{left:0;top:2613px;width:1200px;height:156px;background:var(--dark);color:var(--white)}
.footer-logo{left:180px;top:55px;font-size:44px;font-weight:300;letter-spacing:2px}
.footer-note{left:433px;top:69px;font-size:12px;line-height:19px}
.footer-links{left:787px;top:80px;display:flex;gap:19px;font-size:12px}
.footer-copy{left:0;width:1200px;top:136px;text-align:center;font-size:11.5px}
</style>
</head>
<body>
<div class="page">

  <div class="hero-glow" role="img" aria-label="Soft blue and pink particle glow behind the hero"></div>

  <header>
    <div class="abs nav-logo">tralom</div>
    <nav class="abs nav-links"><span>About</span><span>Technology</span><span>Work With Us</span></nav>
    <div class="abs nav-cta">Get In Touch</div>
  </header>

  <section class="hero">
    <div class="abs hero-mark">tralom</div>
    <h1 class="abs hero-title">Vascular Imaging, Reimagined</h1>
    <p class="abs hero-sub">Tralom Is A Medical Imaging, Deep Learning And Robotics Company On A Mission To Improve<br>Lives By Developing The Next Generation Of Vascular Imaging Solutions</p>
  </section>

  <div class="abs partners">
    <span>Meridane Care</span>
    <span>Corvalis Lab</span>
    <span>Halden Exercise Centre</span>
    <span>Kestrel</span>
    <span>Westmere Vascular</span>
    <span>Novaclan</span>
  </div>

  <section class="about">
    <div class="abs about-photo" role="img" aria-label="Close-up photograph of a red vascular network"></div>
    <h2 class="abs about-title">Learn About The World-Leading Research That Inspired Tralom.</h2>
    <p class="abs about-text body-text">Our Founders Met While Completing Their PhDs At The University Of Carrowdale.<br>Declan, A Physicist, And Marcus, A Biomedical Engineer, Modelled Real Patient Blood Flows To Detect The Onset Of Vascular Disease. Together They Developed The Tech To Scan Patients With A Custom System, As Well As Automating The Construction Of Flow Models For Every Single Scan.<br>Together, They Captured Vascular Disease Progression Within Real Patients' Vessels, Allowing For Before And After Models To Be Created For The First Time, As Well As Building The Largest Dataset Of Realistic Flow Models.</p>
    <div class="btn-dark" style="left:577px;top:919px;width:149px;height:32px">Read More About Us</div>
  </section>

  <div class="burst" style="left:-40px;top:960px;width:320px;height:320px"></div>
  <div class="burst" style="left:978px;top:1248px;width:140px;height:140px"></div>

  <section class="solutions">
    <h2 class="abs section-title" style="top:1055px">Our Solutions</h2>
    <div class="solution" style="left:173px">
      <div class="icon"><svg width="30" height="30" viewBox="0 0 30 30" fill="none" stroke="#1d3a4a" stroke-width="1.3"><path d="M15 4v22M15 10l-7-4M15 14l8-5M15 18l-8 3M15 22l7 2M8 6l-3 3M23 9l3-2"/></svg></div>
      <h3>For Vascular Labs</h3>
      <p>Boost The Consistency And Speed Of Ultrasound Procedures</p>
      <div class="btn-outline">Learn More</div>
    </div>
    <div class="solution" style="left:467px">
      <div class="icon"><svg width="30" height="30" viewBox="0 0 30 30" fill="none" stroke="#1d3a4a" stroke-width="1.3"><rect x="7" y="8" width="16" height="16" rx="1"/><path d="M10 12h4M10 16h4M17 12h3v8h-3zM10 20h4M12 4v4M18 4v4"/></svg></div>
      <h3>For Dialysis Providers</h3>
      <p>Monitor Vascular Access Health Accurately At The Point-Of-Care</p>
      <div class="btn-outline">Learn More</div>
    </div>
    <div class="solution" style="left:760px">
      <div class="icon"><svg width="30" height="30" viewBox="0 0 30 30" fill="none" stroke="#1d3a4a" stroke-width="1.3"><circle cx="15" cy="11" r="5"/><path d="M6 26c1-6 5-8 9-8s8 2 9 8M12 19v4M18 19v4"/></svg></div>
      <h3>For Healthcare Professionals</h3>
      <p>Boost The Consistency And Speed Of Ultrasound Procedures</p>
      <div class="btn-outline">Learn More</div>
    </div>
  </section>

  <section class="products">
    <h2 class="abs section-title" style="top:1423px">Our Products</h2>
    <div class="product" style="left:173px">
      <div class="art" role="img" aria-label="Illustration of a cell with blue and red branching filaments" style="background:radial-gradient(circle,#f08a3c 0,#c94a6a 30%,rgba(70,90,200,.5) 55%,rgba(38,38,38,0) 72%)"></div>
      <h3>Hardware Prodtcs</h3>
      <p>Our Imaging Robot Can Take An Automated Scan Of The Vascular Access At Any Dialysis Provision. Smarter Vascular Status.<br>Our AI Will Show A Live Vascular Access Health Status...</p>
      <div class="btn-outline-light">Read More</div>
    </div>
    <div class="product" style="left:613px">
      <div class="art" role="img" aria-label="3D rendered model of a red vessel segment" style="border-radius:40%;background:radial-gradient(ellipse at 50% 45%,#c0304a 0,#7d1a2c 40%,rgba(38,38,38,0) 70%)"></div>
      <h3>Software Prodtcs</h3>
      <p>Our Imaging Robot Can Take An Automated Scan Of The Vascular Access At Any Dialysis Provision. Smarter Vascular Status.<br>Our AI Will Show A Live Vascular Access Health Status...</p>
      <div class="btn-outline-light">Read More</div>
    </div>
  </section>

  <section class="abs vision">
    <div class="abs vision-art" role="img" aria-label="3D illustration of a blue spherical virus particle"></div>
    <h2 class="abs vision-title">OUR VISION</h2>
    <p class="abs vision-text body-text">Patients Face Long Waits For Outsourced AVF Pre-Mapping Scans<br>High Catheter Rates Drive Infection Risk And Lower Provider Reimbursement<br>Undetected Vascular Access Failures Lead To Medical Emergencies.Patients Can Access In-House, On-The-Spot AVF Pre-Mapping Scans<br>Higher AVF Rates Reduce Infection Risk And Drive Higher Provider Reimbursement<br>Continuous Monitoring Of Vascular Access Health Reduces Unexpected Failures And Emergencies</p>
    <div class="btn-dark" style="left:353px;top:234px;width:156px;height:32px">Register Your Interest</div>
  </section>

  <section class="contact">
    <h2 class="abs contact-title">Contact Us</h2>
    <div class="label" style="top:2226px">FULL NAME*</div>
    <div class="field" style="top:2247px">Name</div>
    <div class="label" style="top:2294px">EMAIL ADDRESS*</div>
    <div class="field" style="top:2315px">Email Address</div>
    <div class="label" style="top:2363px">PHONE NUMBER*</div>
    <div class="field" style="top:2384px;padding-left:82px"><div class="phone-code"><span class="flag"></span>+91 ▾</div>Phone Number</div>
    <div class="abs check"><span></span>Keep me updated on news and offers</div>
    <div class="btn-dark" style="left:174px;top:2472px;width:103px;height:32px">Submit Now</div>

    <div class="photo" role="img" aria-label="Photo of the two founders standing side by side" style="left:629px;top:2263px;width:190px;height:163px;background:linear-gradient(180deg,#ecebe9,#d9d4cf)"></div>
    <div class="photo" role="img" aria-label="Photo of two surgeons in scrubs talking in a hospital" style="left:835px;top:2176px;width:192px;height:162px;background:linear-gradient(160deg,#7e8d98,#4d5e6c)"></div>
    <div class="photo" role="img" aria-label="Illustration of a DNA helix inside a glass sphere" style="left:836px;top:2357px;width:164px;height:162px;border-radius:50%;background:radial-gradient(circle,#e4f2fb 0,#a9d3ee 60%,#d9ecf7 100%)"></div>
  </section>

  <footer class="abs footer">
    <div class="abs footer-logo">tralom</div>
    <p class="abs footer-note">For Use By Qualified Healthcare Professionals Only.<br>Tralom Products Not Yet Available For General Supply.</p>
    <nav class="abs footer-links"><span>Contact</span><span>Work With Us</span><span>Privacy Policy</span></nav>
    <p class="abs footer-copy">© 2025 TRALOM PTY LTD All Rights Reserved</p>
  </footer>

</div>
</body>
</html>
```